AMAZING BLACK FRIDAY AD FOR PRINT OR THE WEB

Create a Black Friday ad for nitrile gloves. We are offering a box of 100, no-powder, exam grade nitrile gloves, for $9.99. No limit. Each case is $99. Create something simple, eye catching, cool. BrisaVeil.com. Sale ends on December 4th. While supplies last. We are a local medical supply company in Hawaii that serves the general public in addition to local businesses, government, etc. Gloves are in short supply and we have tons of inventory ready to sell.

Target Market(s)

Businesses that use supplies such as gloves

Industry/Entity Type

medical supplies

Requirements
Must have
• logo and website

```html
<!DOCTYPE html>
<html lang="en">
<head>
<meta charset="utf-8">
<title>Black Friday Glove Sale – BrisaVeil.com</title>
<link href="https://fonts.googleapis.com/css2?family=Anton&family=Lato:wght@400;700&family=Montserrat:wght@600;800;900&display=swap" rel="stylesheet">
<style>
  :root {
    --backdrop: #4a4a4a;
    --ink: #1b1b1b;
    --green: #00944a;
    --white: #ffffff;
    --grey: #6e6e6e;
  }
  * { margin: 0; padding: 0; box-sizing: border-box; }
  html, body {
    width: 1200px; height: 1200px; overflow: hidden;
    background: var(--backdrop);
  }
  .ad {
    position: absolute; left: 172px; top: 0;
    width: 856px; height: 1200px;
    background: var(--ink);
    color: var(--white);
    font-family: "Lato", sans-serif;
  }
  .headline-panel {
    position: absolute; left: 137px; top: 145px;
    width: 585px; height: 313px;
    background: var(--white);
  }
  .headline-frame {
    position: absolute; left: 22px; top: 27px;
    width: 536px; height: 264px;
    border: 10px solid var(--ink);
  }
  .headline {
    position: absolute; left: 73px;
    font-family: "Montserrat", sans-serif; font-weight: 900;
    font-size: 94px; line-height: 1; letter-spacing: -1px;
  }
  .headline--black { top: 34px; color: var(--ink); }
  .headline--friday { top: 133px; color: var(--green); }

  .price-tag {
    position: absolute; left: 117px; top: 493px;
    width: 301px; height: 148px;
    border: 2px solid var(--white); border-radius: 28px;
    display: flex; align-items: center; justify-content: center;
  }
  .price {
    font-family: "Anton", sans-serif; font-size: 118px; line-height: 1;
    color: var(--green); letter-spacing: -1px;
  }
  .offer-title {
    position: absolute; left: 435px; top: 515px;
    font-family: "Montserrat", sans-serif; font-weight: 600;
    font-size: 46px; line-height: 1; color: var(--white);
  }
  .offer-detail {
    position: absolute; left: 435px; top: 565px;
    font-size: 24px; line-height: 30px; color: var(--green);
  }

  .deadline {
    position: absolute; left: 217px; top: 684px;
    width: 411px; height: 102px;
    display: flex; background: var(--white);
  }
  .deadline-label {
    width: 142px; background: var(--green);
    font-family: "Montserrat", sans-serif; font-weight: 800;
    font-size: 38px; line-height: 40px; color: var(--white);
    padding: 10px 0 0 12px;
  }
  .deadline-date {
    flex: 1; display: flex; align-items: center; justify-content: center;
    font-size: 33px; color: var(--ink); letter-spacing: -0.5px;
  }
  .deadline-date strong { font-weight: 700; margin-left: 8px; }

  .terms {
    position: absolute; left: 203px; top: 829px;
    width: 421px; height: 59px;
    border: 2px solid var(--white);
    display: flex; align-items: center; justify-content: center;
    font-size: 31px; white-space: nowrap;
  }
  .terms .divider { margin: 0 18px; }

  .about {
    position: absolute; left: 90px; top: 914px;
    width: 700px; font-size: 18.5px; line-height: 23.5px;
  }

  .brand {
    position: absolute; left: 0; top: 1060px; width: 856px;
    display: flex; align-items: center; justify-content: center; gap: 14px;
    font-family: "Montserrat", sans-serif; font-weight: 800;
    font-size: 54px; line-height: 1; color: var(--green); letter-spacing: -1px;
  }
  .brand-dot {
    width: 22px; height: 22px; border-radius: 50%; background: var(--green);
  }
</style>
</head>
<body>
  <main class="ad">
    <section class="headline-panel">
      <div class="headline-frame"></div>
      <h1>
        <span class="headline headline--black">BLACK</span>
        <span class="headline headline--friday">FRIDAY</span>
      </h1>
    </section>

    <div class="price-tag"><span class="price">$9.99</span></div>
    <h2 class="offer-title">Box of 100</h2>
    <p class="offer-detail">no-powder, exam grade<br>nitrile gloves</p>

    <div class="deadline">
      <div class="deadline-label">SALE<br>ENDS</div>
      <div class="deadline-date">DECEMBER<strong>4TH</strong></div>
    </div>

    <div class="terms">No limit<span class="divider">|</span>Each case is $99</div>

    <p class="about">We are a local medical supply company in Hawaii that serves the general public in addition to local businesses, government, etc. Gloves are in short supply and we have tons of inventory ready to sell.</p>

    <div class="brand"><span class="brand-dot"></span>BrisaVeil.com</div>
  </main>
</body>
</html>
```